Fast growing Tech company needs redesign of Veltrana's end user website!

We need to have our login screen, the dashboard, and the one page of the Veltrana site to be redesigned for the end-users. Veltrana is a document hosting service for title companies and real estate law firms. This allows the buyers and sellers to view their closing documents after closing along with many other features that help them out during the closing of their property. More information about what we do can be found on our test site https://qpx.524.sampledraft-host.com/. PLEASE NOTE: THE ABOVE SITE IS NOT THE ONE WE NEED REDONE. The above site is our corporate site that explains our service offering and we thought it would be helpful in providing you a better understanding of our service.
The site that we want to have redesigned is for the end user. THE SITE THAT NEEDS TO BE REDONE ARE THE SCREENSHOTS ATTACHED. We will need the login screen, dashboard, and the one page redesigned.
.
We will just need this in HTML and we will then do the rest for the placeholders for logos, data, mapping etc.
Overall, we want a new, fresh, and modern look for the website and we want the login screen, dashboard and one page website to be consistent in design. Again, these are the three screenshots that are attached.
For the winner, we will most likely need to hire you again for more sites because we have other versions.
Thank you and if any questions, please let us know.
Target Market(s)
This site is for buyer and sellers during the closing process of real estate transaction.

```html
<!DOCTYPE html>
<html lang="en">
<head>
<meta charset="utf-8">
<title>Veltrana – End User Screens</title>
<link href="https://fonts.googleapis.com/css2?family=Roboto:wght@400;500;700&family=Lato:wght@400;700&display=swap" rel="stylesheet">
<style>
:root{
  --sheet:#6b6a6b;
  --blue:#2458a8;
  --blue-soft:#4c7fc7;
  --green:#2fb34c;
  --ink:#111;
  --text:#333;
  --muted:#555;
  --white:#fff;
  --panel-foot:#3a3a3c;
  --pale:#dbe6f6;
  --gray-line:#a9a9a9;
  --portrait:#c4c4c4;
}
*{box-sizing:border-box;margin:0;padding:0}
html,body{width:735px;height:1200px;overflow:hidden;background:var(--sheet)}
body{position:relative;font-family:'Lato',sans-serif;color:var(--text)}
.abs{position:absolute}
.head{font-family:'Roboto',sans-serif;font-weight:700;color:var(--ink)}
.c{text-align:center}
.pill{position:absolute;background:var(--blue);color:var(--white);border-radius:8px;font-family:'Roboto',sans-serif;font-weight:700;display:flex;align-items:center;justify-content:center;gap:3px}
.dot{display:inline-block;width:4px;height:4px;border-radius:50%;background:currentColor}

/* one-page site */
.site{position:absolute;left:7px;top:7px;width:358px;height:1186px;background:var(--white);overflow:hidden}
.topbar{position:absolute;left:0;top:0;width:358px;height:21px;background:var(--white)}
.brand{position:absolute;font-family:'Roboto',sans-serif;font-weight:500;color:var(--blue)}
.partner{position:absolute;top:6px;width:16px;height:9px;background:#8a8a8a;border-radius:1px}
.burger{position:absolute;left:318px;top:7px;width:6px;height:6px;border-top:1.5px solid #222;border-bottom:1.5px solid #222}
.burger::after{content:"";position:absolute;left:0;top:1.2px;width:6px;height:1.5px;background:#222}
.hero{position:absolute;left:0;top:21px;width:358px;height:166px;background:linear-gradient(180deg,#4a5466 0%,#5a5f66 45%,#3f4a3a 100%)}
.hero-title{position:absolute;left:0;width:358px;top:55px;font-size:13px;color:var(--white)}
.hero-sub{position:absolute;left:0;width:358px;top:74px;font-size:4.4px;line-height:9px;color:#eee;font-family:'Roboto',sans-serif}
.welcome-photo{position:absolute;left:50px;top:214px;width:92px;height:92px;border-radius:50%;background:linear-gradient(180deg,#5f97d8 0%,#a6c6e8 40%,#9a6e5a 58%,#4b7f3a 100%)}
.welcome-title{position:absolute;left:178px;top:217px;font-size:10.5px}
.para{position:absolute;font-size:4.2px;line-height:8.9px;color:#333}
.instructions{position:absolute;left:0;top:336px;width:358px;height:195px;background:linear-gradient(180deg,#c9daf4,#e5ecf6 60%,#d5e0ef)}
.section-title{position:absolute;left:0;width:358px;font-size:10.5px}
.card{position:absolute;top:382px;width:70px;height:126px;background:var(--white);border-radius:5px;overflow:hidden;box-shadow:0 1px 3px rgba(0,0,0,.15)}
.card .ph{height:65px}
.card h3{font-family:'Roboto',sans-serif;font-weight:700;font-size:5.3px;line-height:8.5px;color:#111;margin:3px 4px 0}
.card p{font-size:4.2px;line-height:7.2px;margin:1px 4px 0;color:#333}
.card .more{position:absolute;left:4px;bottom:5px;font-family:'Roboto',sans-serif;font-weight:700;font-size:4.6px;color:var(--blue)}
.faq{position:absolute;left:64px;width:229px;height:23px;background:var(--white);box-shadow:0 1px 4px rgba(0,0,0,.18);font-size:4.3px;display:flex;align-items:center;justify-content:space-between;padding:0 7px}
.faq .tg{width:4px;height:4px;border-radius:50%;background:var(--blue)}
.band{position:absolute;left:0;top:817px;width:358px;height:5px;background:var(--gray-line)}
.ms-label{position:absolute;width:80px;margin-left:-40px;font-family:'Roboto',sans-serif;font-size:4.5px;color:#111;text-align:center;line-height:6px}
.ms-label small{display:block;font-size:3.8px;color:#444}
.ms-ico{position:absolute;width:14px;height:12px;margin-left:-7px;border:1px solid var(--blue);border-radius:2px}
.vdots{position:absolute;width:0;border-left:1px dotted #333;margin-left:-.5px}
.node{position:absolute;top:816px;width:5px;height:5px;margin-left:-2.5px;border-radius:50%;background:var(--white);border:.8px solid var(--blue)}
.member{position:absolute;width:90px;margin-left:-45px;text-align:center}
.avatar{width:76px;height:76px;margin:0 auto;border-radius:50%;background:var(--portrait)}
.member h4{font-family:'Roboto',sans-serif;font-weight:700;font-size:6.5px;color:#111;margin-top:7px}
.member .firm{font-size:3.8px;margin-top:2px;color:#444}
.member p{font-size:4.2px;line-height:7.6px;margin-top:3px;color:#444}
.socials{display:flex;gap:3.5px;justify-content:center;margin-top:3px}
.socials i,.foot-socials i{width:3.5px;height:3.5px;border-radius:50%;background:var(--blue);display:block}
.footer{position:absolute;left:0;top:1072px;width:358px;height:114px;background:#000;color:var(--white)}

/* auth screens */
.screen{position:absolute;left:371px;width:358px;height:225px;overflow:hidden}
.screen .foot{position:absolute;left:0;top:206px;width:358px;height:19px;background:var(--panel-foot);color:#eee;font-family:'Roboto',sans-serif;font-size:4.3px;display:flex;align-items:center;justify-content:center}
.signup{position:absolute;left:293px;top:15px;width:29px;height:10px;border-radius:5px;background:var(--blue);color:#fff;font-size:4.2px;display:flex;align-items:center;justify-content:center}
.tagline{position:absolute;font-size:3.4px;color:#ddd}
.field-label{position:absolute;left:12px;font-size:4.5px;color:#444}
.field{position:absolute;left:11px;width:101px;height:11px;border:.6px solid #999;border-radius:2px}
.field i{position:absolute;left:4px;top:3.5px;width:3px;height:3.5px;background:#222;border-radius:1px}
</style>
</head>
<body>

<!-- ONE-PAGE SITE -->
<main class="site">
  <header class="topbar">
    <div class="brand" style="left:30px;top:4px;font-size:8px">Veltrana</div>
    <div class="abs" style="left:31px;top:14px;font-size:2.6px;color:#333">staying in the loop</div>
    <span class="partner" style="left:82px"></span>
    <span class="partner" style="left:115px"></span>
    <span class="partner" style="left:148px"></span>
    <span class="partner" style="left:181px"></span>
    <span class="partner" style="left:210px;width:25px"></span>
    <span class="partner" style="left:247px"></span>
    <span class="partner" style="left:273px;width:22px"></span>
    <span class="burger"></span>
  </header>

  <section class="hero" role="img" aria-label="Row of suburban townhouses under a blue sky, darkened"></section>
  <h1 class="hero-title head c" style="color:#fff">Veltrana Staying in the loop</h1>
  <p class="hero-sub c">Lorem ipsum dolor sit amet, consectetur adipiscing elit, sed do eiusmod<br>tempor incididunt ut labore et dolore magna aliqua.</p>
  <a class="pill" style="left:156px;top:117px;width:52px;height:12px;font-size:4.6px;border-radius:6px">LEARN MORE <span class="dot"></span></a>

  <!-- welcome -->
  <div class="welcome-photo" role="img" aria-label="Colourful two-storey house with white picket fence"></div>
  <h2 class="welcome-title head">Welcome Quinn Buyer</h2>
  <p class="para" style="left:178px;top:236px;width:152px">Lorem ipsum dolor sit amet, consectetur adipiscing elit, sed do eiusmod tempor incididunt ut labore et dolore magna aliqua. Ut enim ad minim veniam, quis nostrud exercitation ullamco laboris nisi ut aliquip ex ea commodo consequat. Duis aute irure dolor in reprehenderit in voluptate velit esse cillum dolore eu fugiat nulla pariatur.</p>
  <a class="pill" style="left:179px;top:292px;width:95px;height:13px;font-size:4.6px;border-radius:6.5px">GET YOUR TRANSACTION DETAILS <span class="dot"></span></a>

  <!-- instructions -->
  <section class="instructions" aria-label="Instructions"></section>
  <h2 class="section-title head c" style="top:352px">Veltrana Instructions</h2>
  <article class="card" style="left:31px"><div class="ph" role="img" aria-label="Hands typing on a laptop with document overlay" style="background:linear-gradient(135deg,#1e3048,#3d5a78)"></div><h3>Documents you need to view</h3><p>Lorem ipsum dolor sit amet, consectetur adipiscing elit, sed do eiusmod tempor</p><span class="more">LEARN MORE ●</span></article>
  <article class="card" style="left:107px"><div class="ph" role="img" aria-label="Person signing paperwork at a desk" style="background:linear-gradient(135deg,#3e4a55,#8b9299)"></div><h3>Wiring Instructions</h3><p>Lorem ipsum dolor sit amet, consectetur adipiscing elit, sed do eiusmod tempor incididunt ut labore et dolore magna</p><span class="more">LEARN MORE ●</span></article>
  <article class="card" style="left:182px"><div class="ph" role="img" aria-label="Checklist clipboard and pen on a wooden table" style="background:linear-gradient(135deg,#7a4a26,#c79a63)"></div><h3>Moving Checklist</h3><p>Lorem ipsum dolor sit amet, consectetur adipiscing elit, sed do eiusmod tempor incididunt ut labore et dolore magna</p><span class="more">LEARN MORE ●</span></article>
  <article class="card" style="left:258px"><div class="ph" role="img" aria-label="Hand writing on a form next to a laptop" style="background:linear-gradient(135deg,#5a5350,#a9a39e)"></div><h3>Moving Wishlist</h3><p>Lorem ipsum dolor sit amet, consectetur adipiscing elit, sed do eiusmod tempor incididunt ut labore et dolore magna</p><span class="more">LEARN MORE ●</span></article>

  <!-- faq -->
  <h2 class="section-title head c" style="top:554px;left:3px">FAQ</h2>
  <div class="faq" style="top:581px"><span>Lorem IpsumLorem ipsum dolor sit amet, consectetur adipiscing elit</span><span class="tg"></span></div>
  <div class="faq" style="top:609px"><span>Lorem IpsumLorem ipsum dolor sit amet, consectetur adipiscing elit</span><span class="tg"></span></div>
  <div class="faq" style="top:637px"><span>Lorem IpsumLorem ipsum dolor sit amet, consectetur adipiscing elit</span><span class="tg"></span></div>
  <div class="faq" style="top:665px"><span>Lorem IpsumLorem ipsum dolor sit amet, consectetur adipiscing elit</span><span class="tg"></span></div>
  <div class="faq" style="top:693px"><span>Lorem IpsumLorem ipsum dolor sit amet, consectetur adipiscing elit</span><span class="tg"></span></div>

  <!-- milestones -->
  <h2 class="section-title head c" style="top:741px">Closing Milestones</h2>
  <div class="band"></div>
  <svg class="abs" style="left:49px;top:816px" width="264" height="7" viewBox="0 0 264 7" aria-hidden="true">
    <polygon points="0,0 42,0 45,3.5 42,7 0,7 3,3.5" fill="#2458a8"/>
    <polygon points="44,0 86,0 89,3.5 86,7 44,7 47,3.5" fill="#2fb34c"/>
    <polygon points="88,0 130,0 133,3.5 130,7 88,7 91,3.5" fill="#2458a8"/>
    <polygon points="132,0 174,0 177,3.5 174,7 132,7 135,3.5" fill="#2fb34c"/>
    <polygon points="176,0 218,0 221,3.5 218,7 176,7 179,3.5" fill="#2458a8"/>
    <polygon points="220,0 258,0 261,3.5 258,7 220,7 223,3.5" fill="#2fb34c"/>
  </svg>
  <span class="node" style="left:70px"></span><span class="node" style="left:113px"></span><span class="node" style="left:157px"></span>
  <span class="node" style="left:200px"></span><span class="node" style="left:244px"></span><span class="node" style="left:288px"></span>

  <span class="ms-ico" style="left:70px;top:767px;border-radius:50%"></span>
  <div class="ms-label" style="left:70px;top:785px">Transaction started<small>Completed</small></div>
  <span class="vdots" style="left:70px;top:802px;height:12px"></span>
  <span class="ms-ico" style="left:157px;top:767px"></span>
  <div class="ms-label" style="left:157px;top:785px">Delivered Title Report<small>Not Completed</small></div>
  <span class="vdots" style="left:157px;top:802px;height:12px"></span>
  <span class="ms-ico" style="left:244px;top:767px"></span>
  <div class="ms-label" style="left:244px;top:785px">Signing Scheduled<small>Not Completed</small></div>
  <span class="vdots" style="left:244px;top:802px;height:12px"></span>

  <span class="vdots" style="left:113px;top:824px;height:12px"></span>
  <span class="ms-ico" style="left:113px;top:838px;border-radius:50%"></span>
  <div class="ms-label" style="left:113px;top:856px">Earnest Money Received<small>Completed</small></div>
  <span class="vdots" style="left:200px;top:824px;height:12px"></span>
  <span class="ms-ico" style="left:200px;top:838px"></span>
  <div class="ms-label" style="left:200px;top:856px">Title Cleared<small>Not Completed</small></div>
  <span class="vdots" style="left:288px;top:824px;height:12px"></span>
  <span class="ms-ico" style="left:288px;top:838px;width:18px;margin-left:-9px"></span>
  <div class="ms-label" style="left:288px;top:856px">Transaction Closed<small>Not Completed</small></div>

  <!-- team -->
  <h2 class="section-title head c" style="top:891px">Our Team</h2>
  <div class="member" style="left:92px;top:922px"><div class="avatar" role="img" aria-label="Portrait photo of team member"></div><h4>Nora Halvik</h4><div class="firm">The Real Estate Law Firm</div><p>Lorem ipsum dolor sit amet,<br>consectetur adipiscing elit,</p><div class="socials"><i></i><i></i><i></i><i></i></div></div>
  <div class="member" style="left:179px;top:922px"><div class="avatar" role="img" aria-label="Portrait photo of team member"></div><h4>Dale Buyer Agent</h4><div class="firm">Dales Real Estate</div><p>Lorem ipsum dolor sit amet,<br>consectetur adipiscing elit,</p><div class="socials"><i></i><i></i><i></i><i></i></div></div>
  <div class="member" style="left:266px;top:922px"><div class="avatar" role="img" aria-label="Portrait photo of team member"></div><h4>Omar Loanofficer</h4><div class="firm">Omar Mortgages</div><p>Lorem ipsum dolor sit amet,<br>consectetur adipiscing elit,</p><div class="socials"><i></i><i></i><i></i><i></i></div></div>

  <!-- footer -->
  <footer class="footer">
    <h3 class="abs c" style="left:0;width:358px;top:18px;font-family:'Roboto',sans-serif;font-weight:700;font-size:6.5px">SUBSCRIBE NEWSLETTER</h3>
    <div class="abs" style="left:106px;top:39px;width:146px;height:13px;border-radius:6.5px;background:#fff;font-size:4.3px;color:#888;padding:4.3px 8px">Enter Your Email</div>
    <div class="pill" style="left:216px;top:39px;width:36px;height:13px;border-radius:6.5px;font-size:4.5px">SUBMIT <span class="dot"></span></div>
    <div class="abs" style="left:104px;top:67px;display:flex;gap:8px;align-items:center;font-size:4.2px">
      <span>✉ Sed ut perspiciatis unde omnis</span>
      <span style="font-family:'Roboto',sans-serif;font-weight:700">☎ 155-555-0142</span>
      <span class="foot-socials" style="display:flex;gap:4px"><i></i><i></i><i></i><i></i></span>
    </div>
    <div class="abs" style="left:34px;top:84px;width:290px;height:.5px;background:#333"></div>
    <div class="abs c" style="left:0;width:358px;top:96px;font-size:4.2px">©Copyrights 2021 Company Name &nbsp;|&nbsp; All Rights Reserved</div>
  </footer>
</main>

<!-- LOGIN SCREEN -->
<section class="screen" style="top:372px" aria-label="Login">
  <div class="abs" role="img" aria-label="Glass office towers seen from below against a night sky" style="left:0;top:0;width:358px;height:206px;background:linear-gradient(160deg,#1a2438 0%,#2a3d60 40%,#142033 100%)"></div>
  <div class="brand" style="left:24px;top:10px;font-size:9px;color:#fff">Veltrana</div>
  <div class="tagline" style="left:24px;top:26px">staying in the loop</div>
  <div class="signup">SIGN UP</div>
  <div class="abs" style="left:118px;top:52px;width:124px;height:126px;background:#fff;border-radius:5px">
    <div class="abs head c" style="left:0;width:124px;top:15px;font-size:6.3px;font-weight:500">Welcome back</div>
    <div class="field-label" style="top:29px">Username</div>
    <div class="field" style="top:36px"><i></i></div>
    <div class="field-label" style="top:53px">Password</div>
    <div class="field" style="top:60px"><i></i></div>
    <div class="abs" style="left:11px;top:78px;font-size:4.2px;color:#555;display:flex;align-items:center;gap:3px"><span style="width:4.5px;height:4.5px;border:.6px solid #888;display:inline-block"></span>Remember Me</div>
    <div class="abs" style="left:75px;top:78px;font-size:4.2px;color:#555">● Forget Password</div>
    <div class="abs" style="left:11px;top:98px;width:29px;height:11px;border:.8px solid var(--blue);border-radius:6px;font-size:4.2px;color:var(--blue);display:flex;align-items:center;justify-content:center">LOG IN</div>
  </div>
  <div class="foot">©Copyrights 2021 Veltrana &nbsp;|&nbsp; All Rights Reserved</div>
</section>

<!-- PROPERTY SELECT SCREEN -->
<section class="screen" style="top:603px" aria-label="Property selection">
  <div class="abs" role="img" aria-label="Large suburban house with green lawn under a cloudy sky" style="left:0;top:0;width:358px;height:206px;background:linear-gradient(180deg,#6d7b8e 0%,#8a9099 35%,#4b4a40 60%,#3e5a28 100%)"></div>
  <div class="brand" style="left:24px;top:10px;font-size:9px;color:#fff">Veltrana</div>
  <div class="tagline" style="left:24px;top:26px">staying in the loop</div>
  <div class="signup">SIGN UP</div>
  <div class="abs" style="left:70px;top:79px;width:218px;height:65px;background:#fff;border-radius:4px">
    <div class="abs" style="left:90px;top:0;width:.6px;height:65px;background:#ddd"></div>
    <div class="brand c" style="left:0;width:90px;top:16px;font-size:16px">Veltrana</div>
    <div class="abs c" style="left:0;width:90px;top:46px;font-size:6px;color:#777">staying in the loop</div>
    <div class="abs head" style="left:107px;top:8px;font-size:5px;line-height:9px;font-weight:500">WELCOME TO THE<br>DIGITAL CLOSING PACKAGE</div>
    <div class="abs" style="left:107px;top:29px;width:91px;height:9px;border:.6px solid #bbb;border-radius:2px;font-size:3.6px;color:#555;padding:2.4px 4px">Select A property...<span style="float:right">⇕</span></div>
    <div class="pill" style="left:107px;top:47px;width:41px;height:9px;border-radius:4.5px;font-size:3.8px;font-weight:400">Enter &nbsp; ›</div>
  </div>
  <div class="foot">©Copyrights 2021 Veltrana &nbsp;|&nbsp; All Rights Reserved</div>
</section>

</body>
</html>
```